Company Letter head for real estate company

need company letter head
Updates

You can use the logo that I submitted. no need to create a new one

Requirements
Must have
• must have my address on it..38264 WINDMERE, CANTON, MI 48302-1175, INFO@MUVRO.CA

```html
<!DOCTYPE html>
<html lang="en">
<head>
<meta charset="utf-8">
<title>Muvro Letterhead</title>
<link href="https://fonts.googleapis.com/css2?family=Open+Sans:wght@400;600&family=Pinyon+Script&display=swap" rel="stylesheet">
<style>
  :root {
    --backdrop: #e9eaea;
    --paper: #f7f7f6;
    --green-deep: #5b8a45;
    --green-bright: #7cbf3f;
    --ink: #3a3a3a;
    --ink-soft: #555;
  }
  * { margin: 0; padding: 0; box-sizing: border-box; }
  html, body { width: 1200px; height: 795px; overflow: hidden; background: var(--backdrop); }
  body { position: relative; font-family: "Open Sans", sans-serif; color: var(--ink); }

  .letterhead {
    position: absolute; left: 320px; top: 15px;
    width: 560px; height: 765px;
    background: var(--paper);
    box-shadow: 0 6px 24px rgba(0,0,0,.12);
    overflow: hidden;
  }
  .letterhead__swoosh { position: absolute; inset: 0; width: 100%; height: 100%; }

  .brand {
    position: absolute; left: 50px; top: 56px;
    display: flex; align-items: center; gap: 8px;
    font-size: 22px; font-weight: 600; letter-spacing: 2px; color: var(--ink);
  }
  .brand__dot { width: 12px; height: 12px; border-radius: 50%; background: var(--green-bright); }

  .letter {
    position: absolute; left: 62px; top: 140px; width: 310px;
    font-size: 8.6px; line-height: 1.55; color: var(--ink-soft);
  }
  .letter__greeting { margin-bottom: 8px; }
  .letter p { margin-bottom: 14px; }
  .letter__closing { margin-top: 18px; }
  .letter__signature {
    font-family: "Pinyon Script", cursive; font-size: 24px; color: #222;
    margin-top: 2px; padding-left: 14px;
  }

  .contact {
    position: absolute; top: 660px; font-size: 9.5px; line-height: 1.45; color: var(--ink-soft);
  }
  .contact::before {
    content: ""; display: block; width: 26px; height: 2px; background: var(--green-bright); margin-bottom: 9px;
  }
  .contact--address { left: 62px; }
  .contact--reach { left: 232px; }
  .contact__company { color: var(--green-bright); }
  .contact__row { display: flex; align-items: center; gap: 6px; }
  .contact__row svg { width: 8px; height: 8px; fill: var(--green-bright); }
</style>
</head>
<body>
  <main class="letterhead">
    <svg class="letterhead__swoosh" viewBox="0 0 560 765" preserveAspectRatio="none" aria-hidden="true">
      <path d="M300 0 H560 V600 C520 430 440 260 300 0 Z" fill="var(--green-bright)"/>
      <path d="M320 0 H560 V585 C525 420 450 250 320 0 Z" fill="var(--green-deep)"/>
    </svg>

    <div class="brand"><span class="brand__dot"></span>MUVRO</div>

    <article class="letter">
      <p class="letter__greeting">Dear Daniel Hartwell,</p>
      <p>Lorem ipsum dolor sit amet, consectetuer adipiscing elit, sed diam nonummy nibh euismod tincidunt ut laoreet dolore magna aliquam erat volutpat. Ut wisi enim ad minim veniam, quis nostrud exerci tation ullamcorper suscipit lobortis nisl ut aliquip ex ea commodo consequat. Duis dolore te feugait nulla facilisi. Nam liber tempor cum soluta nobis eleifend option congue nihil imperdiet doming id quod mazim placerat facer possim assum. Lorem ipsum dolor sit amet, consectetuer adipiscing elit, sed diam nonummy nibh euismod tincidunt ut laoreet dolore magna aliquam erat volutpat. Ut wisi enim ad minim veniam, quis nostrud exerci tation ullamcorper suscipit lobortis nisl ut aliquip ex ea commodo consequat.</p>
      <p>Consectetuer adipiscing elit, sed diam nonummy nibh euismod tincidunt ut laoreet dolore magna aliquam erat volutpat. Ut wisi enim ad minim veniam, quis nostrud exerci tation ullamcorper suscipit lobortis nisl ut aliquip ex ea commodo consequat. Consectetuer adipiscing elit, sed diam nonummy nibh euismod tincidunt ut laoreet dolore magna aliquam erat volutpat. Ut wisi enim ad minim veniam, quis nostrud exerci tation ullamcorper suscipit lobortis nisl ut aliquip ex ea commodo consequat.</p>
      <p>Consectetuer adipiscing elit, sed diam nonummy nibh euismod tincidunt ut laoreet dolore magna aliquam erat volutpat. Ut wisi enim ad minim veniam, quis nostrud exerci tation ullamcorper suscipit lobortis nisl ut aliquip ex ea commodo consequat. Consectetuer adipiscing elit, sed diam nonummy nibh euismod tincidunt ut laoreet dolore magna aliquam erat volutpat. Ut wisi enim ad minim veniam, quis nostrud exerci tation ullamcorper suscipit lobortis nisl ut aliquip ex ea commodo consequat.</p>
      <p class="letter__closing">Sincerely Yours</p>
      <p class="letter__signature">Thomas Avery</p>
    </article>

    <address class="contact contact--address" style="font-style:normal">
      <div class="contact__company">Muvro Land And Property<br>Development Inc.</div>
      <div>38264 Windmere Dr</div>
      <div>Canton, MI 48302-1175</div>
    </address>

    <address class="contact contact--reach" style="font-style:normal">
      <div class="contact__row"><svg viewBox="0 0 10 10"><path d="M2 0.5 L4 2.5 L3 4 C3.8 5.6 4.6 6.4 6 7 L7.5 6 L9.5 8 L8 9.5 C4 9 1 6 0.5 2 Z"/></svg>416.555.0147</div>
      <div class="contact__row"><svg viewBox="0 0 10 10"><path d="M0 2 H10 V8.5 H0 Z M0.6 2.4 L5 5.6 L9.4 2.4" stroke="#fff" stroke-width=".8"/></svg>info@muvro.ca</div>
      <div class="contact__row"><svg viewBox="0 0 10 10"><circle cx="5" cy="5" r="4.8"/></svg>www.muvro.ca</div>
    </address>
  </main>
</body>
</html>
```